Hair Salon using organic products looking for AWSOME new menu's!!

We want different and fun incorporating our logo. We would love a folding or tri-folding menu. Any ideas would be welcome we like different. We are an verbena salon in a little colonial town, but don't like the colonial feel. we would like menu's that would not cost an arm and a leg to print. And we could update as prices and services change without having to re-do the entire design.

Target Market(s)

upper class clients with an interest in using plant based products on their hair and skin

Industry/Entity Type

Hair And Beauty

Requirements
Must have
• Logo, area for contact information and ability to list all salon services
Nice to have
• just a really fun different look to set us aside from other salons. We like to be different

```html
<!DOCTYPE html>
<html lang="en">
<head>
<meta charset="utf-8">
<title>Verbena Salon – Service Menu</title>
<link rel="stylesheet" href="https://fonts.googleapis.com/css2?family=Cinzel:wght@400;600&family=EB+Garamond:ital,wght@0,500;0,700;1,500&display=swap">
<style>
  :root {
    --gold-dark: #a8751f;
    --gold: #c99a2e;
    --gold-mid: #dcb748;
    --gold-light: #f3e37c;
    --gold-soft: #e3cd6a;
    --ink-gold: #8a6414;
    --paper: #ffffff;
    --stripe: #f1f1f3;
    --backdrop: #ececec;
  }
  * { box-sizing: border-box; margin: 0; padding: 0; }
  html, body { width: 1200px; height: 1000px; overflow: hidden; }
  body { background: var(--backdrop); position: relative; font-family: "EB Garamond", Georgia, serif; color: var(--ink-gold); }

  .sheet { position: absolute; width: 700px; height: 470px; box-shadow: 0 6px 18px rgba(0,0,0,.18); overflow: hidden; }
  .sheet--front { left: 30px; top: 20px; padding: 22px; background: linear-gradient(135deg, var(--gold-dark), var(--gold-light) 45%, var(--gold) 70%, var(--gold-dark)); }
  .sheet--back { left: 470px; top: 510px; background: linear-gradient(120deg, var(--gold-dark) 0%, var(--gold) 30%, var(--gold-light) 60%, var(--gold) 85%, var(--gold-dark) 100%); }

  .front-inner { position: relative; width: 100%; height: 100%; background: repeating-linear-gradient(180deg, var(--paper) 0 9px, var(--stripe) 9px 13px); outline: 1px solid var(--gold-soft); outline-offset: -6px; }

  .brand { position: absolute; text-align: center; font-family: "Cinzel", serif; color: var(--gold); letter-spacing: .18em; white-space: nowrap; }
  .brand__mark { display: block; margin: 0 auto 8px; border-radius: 50%; background: var(--gold-mid); }
  .brand--front { left: 22px; top: 40px; width: 180px; font-size: 14px; }
  .brand--front .brand__mark { width: 34px; height: 34px; }

  .menu-box { position: absolute; border: 1px solid var(--gold-soft); background: var(--paper); padding: 20px 10px 6px 14px; overflow: hidden; }
  .menu-box__title { position: absolute; top: -1px; left: 50%; transform: translateX(-50%); background: var(--gold-soft); color: var(--ink-gold); font-family: "Cinzel", serif; font-weight: 600; font-size: 11px; letter-spacing: .06em; padding: 2px 10px; white-space: nowrap; }

  .service { list-style: none; }
  .service__item { position: relative; padding-left: 9px; margin-bottom: 8px; }
  .service__item::before { content: ""; position: absolute; left: 0; top: 5px; width: 4px; height: 4px; border-radius: 50%; background: var(--gold-mid); }
  .service__row { display: flex; align-items: baseline; font-weight: 700; font-size: 10.5px; line-height: 14px; }
  .service__leader { flex: 1; border-bottom: 1px dotted var(--ink-gold); margin: 0 2px; transform: translateY(-2px); }
  .service__price { font-size: 9.5px; font-weight: 500; }
  .service--boxed .service__price { border: 1px solid var(--gold-soft); padding: 0 2px; }
  .service__desc { font-style: italic; font-size: 7.5px; line-height: 9px; padding-left: 22px; margin-top: 1px; }

  .box--styling { left: 40px; top: 140px; width: 180px; height: 278px; }
  .box--coloring { left: 240px; top: 36px; width: 185px; height: 160px; }
  .box--waxing { left: 248px; top: 212px; width: 185px; height: 208px; }
  .box--makeup { left: 445px; top: 14px; width: 180px; height: 292px; }
  .box--coloring .service__item, .box--waxing .service__item { margin-bottom: 12px; }
  .box--makeup .service__item { margin-bottom: 10px; }

  .contact { position: absolute; left: 455px; top: 318px; width: 185px; height: 100px; background: var(--gold-mid); outline: 1px solid var(--paper); outline-offset: -5px; text-align: center; color: var(--paper); padding: 11px 12px; }
  .contact__name { font-family: "Cinzel", serif; font-size: 7px; letter-spacing: .18em; display: flex; align-items: center; justify-content: center; gap: 3px; flex-direction: column; }
  .contact__name .dot { width: 12px; height: 12px; border-radius: 50%; background: var(--paper); opacity: .8; }
  .contact__text { font-style: italic; font-size: 7px; line-height: 1.2; margin: 3px 0 5px; }

  .social { display: flex; gap: 6px; justify-content: center; }
  .social__icon { width: 16px; height: 16px; border-radius: 3px; background: currentColor; }
  .contact .social { color: var(--paper); }

  .back-frame { position: absolute; inset: 10px; border: 1px solid rgba(255,255,255,.55); outline: 1px solid rgba(255,255,255,.35); outline-offset: -5px; }
  .back-decor { position: absolute; border-radius: 50%; background: radial-gradient(circle, rgba(255,240,170,.35), rgba(255,240,170,0) 70%); }
  .back-decor--right { right: -40px; top: 170px; width: 260px; height: 260px; }
  .back-decor--left { left: 150px; top: 10px; width: 200px; height: 200px; }

  .list-panel { position: absolute; left: 20px; top: 0; width: 210px; height: 410px; background: var(--paper); padding: 6px; }
  .list-panel__inner { height: 100%; background: repeating-linear-gradient(180deg, var(--paper) 0 9px, var(--stripe) 9px 13px); border: 1px solid var(--gold-soft); padding: 6px 10px 0 14px; }
  .list-panel .service__item { margin-bottom: 22px; }

  .tips { position: absolute; left: 280px; top: 90px; width: 180px; height: 210px; background: var(--paper); padding: 6px; }
  .tips__inner { height: 100%; border: 1px solid var(--gold-soft); padding: 22px 10px 6px 14px; position: relative; }
  .tips__text { font-style: italic; font-size: 7.4px; line-height: 1.4; position: relative; padding-left: 8px; }
  .tips__text::before { content: ""; position: absolute; left: 0; top: 3px; width: 4px; height: 4px; border-radius: 50%; background: var(--gold-mid); }

  .brand--cover { right: 30px; top: 40px; width: 200px; font-size: 18px; color: var(--paper); }
  .brand--cover .brand__mark { width: 52px; height: 52px; background: rgba(255,255,255,.7); }
  .brand--foot { left: 245px; bottom: 16px; width: 120px; font-size: 7px; color: var(--paper); }
  .brand--foot .brand__mark { width: 16px; height: 16px; background: rgba(255,255,255,.8); margin-bottom: 4px; }

  .social--back { position: absolute; right: 50px; bottom: 16px; color: var(--ink-gold); }
  .social--back .social__icon { width: 18px; height: 18px; }
</style>
</head>
<body>

<section class="sheet sheet--front" aria-label="Menu front">
  <div class="front-inner">
    <div class="brand brand--front"><span class="brand__mark"></span>VERBENA SALON</div>

    <div class="menu-box box--styling">
      <h2 class="menu-box__title">HAIR STYLING</h2>
      <ul class="service service--boxed">
        <li class="service__item"><div class="service__row">Bridal Up Style<span class="service__leader"></span><span class="service__price">$15</span></div><p class="service__desc">Lorem ipsum dolor sit, consectetuer adipiscing.</p></li>
        <li class="service__item"><div class="service__row">Blow Dry<span class="service__leader"></span><span class="service__price">$10</span></div><p class="service__desc">Lorem ipsum dolo r sit, consectetuer adipiscing</p></li>
        <li class="service__item"><div class="service__row">Up Style<span class="service__leader"></span><span class="service__price">$20</span></div><p class="service__desc">Lorem ipsum dolor sit, consectetuer adipiscing.</p></li>
        <li class="service__item"><div class="service__row">Night Style<span class="service__leader"></span><span class="service__price">$15</span></div><p class="service__desc">Lorem ipsum dolor sit, consectetuer adipiscing.</p></li>
        <li class="service__item"><div class="service__row">Super Dry<span class="service__leader"></span><span class="service__price">$10</span></div><p class="service__desc">Lorem ipsum dolo r sit, consectetuer adipiscing</p></li>
        <li class="service__item"><div class="service__row">Diva Style<span class="service__leader"></span><span class="service__price">$20</span></div><p class="service__desc">Lorem ipsum dolor sit, consectetuer adipiscing.</p></li>
      </ul>
    </div>

    <div class="menu-box box--coloring">
      <h2 class="menu-box__title">HAIR COLORING</h2>
      <ul class="service">
        <li class="service__item"><div class="service__row">Single Process Color<span class="service__leader"></span><span class="service__price">$15</span></div><p class="service__desc">Lorem ipsum dolor sit, consectetuer adipiscing.</p></li>
        <li class="service__item"><div class="service__row">Full Highlight<span class="service__leader"></span><span class="service__price">$10</span></div><p class="service__desc">Lorem ipsum dolo r sit, consectetuer adipiscing</p></li>
        <li class="service__item"><div class="service__row">Partial Highlight<span class="service__leader"></span><span class="service__price">$20</span></div><p class="service__desc">Lorem ipsum dolor sit, consectetuer adipiscing.</p></li>
      </ul>
    </div>

    <div class="menu-box box--waxing">
      <h2 class="menu-box__title">WAXING</h2>
      <ul class="service">
        <li class="service__item"><div class="service__row">Eyebrow<span class="service__leader"></span><span class="service__price">$15</span></div><p class="service__desc">Lorem ipsum dolor sit, consectetuer adipiscing.</p></li>
        <li class="service__item"><div class="service__row">Lip<span class="service__leader"></span><span class="service__price">$10</span></div><p class="service__desc">Lorem ipsum dolo r sit, consectetuer adipiscing</p></li>
        <li class="service__item"><div class="service__row">Chin<span class="service__leader"></span><span class="service__price">$20</span></div><p class="service__desc">Lorem ipsum dolor sit, consectetuer adipiscing.</p></li>
        <li class="service__item"><div class="service__row">Cheeks<span class="service__leader"></span><span class="service__price">$20</span></div><p class="service__desc">Lorem ipsum dolor sit, consectetuer adipiscing.</p></li>
      </ul>
    </div>

    <div class="menu-box box--makeup">
      <h2 class="menu-box__title">MAKE-UP</h2>
      <ul class="service">
        <li class="service__item"><div class="service__row">Application<span class="service__leader"></span><span class="service__price">$25</span></div><p class="service__desc">Lorem ipsum dolor sit, consectetuer adipiscing.</p></li>
        <li class="service__item"><div class="service__row">Eye Application<span class="service__leader"></span><span class="service__price">$10</span></div><p class="service__desc">Lorem ipsum dolo r sit, consectetuer adipiscing</p></li>
        <li class="service__item"><div class="service__row">Bridal Make-Up<span class="service__leader"></span><span class="service__price">$20</span></div><p class="service__desc">Lorem ipsum dolor sit, consectetuer adipiscing.</p></li>
        <li class="service__item"><div class="service__row">Make-Up Consultation<span class="service__leader"></span><span class="service__price">$25</span></div><p class="service__desc">Lorem ipsum dolor sit, consectetuer adipiscing.</p></li>
        <li class="service__item"><div class="service__row">Individual Lashes<span class="service__leader"></span><span class="service__price">$10</span></div><p class="service__desc">Lorem ipsum dolo r sit, consectetuer adipiscing</p></li>
        <li class="service__item"><div class="service__row">Nigth Make-Up<span class="service__leader"></span><span class="service__price">$20</span></div><p class="service__desc">Lorem ipsum dolor sit, consectetuer adipiscing.</p></li>
      </ul>
    </div>

    <div class="contact">
      <div class="contact__name"><span class="dot"></span>VERBENA SALON</div>
      <p class="contact__text">Lorem ipsum dolor sit amet, consectetuer adipiscing elit, sed diam nonummy nibh euismod tincidunt ut laoreet dolore magna aliquam erat volutpat.</p>
      <div class="social"><span class="social__icon"></span><span class="social__icon"></span><span class="social__icon"></span><span class="social__icon"></span></div>
    </div>
  </div>
</section>

<section class="sheet sheet--back" aria-label="Menu back">
  <div class="back-decor back-decor--left" role="img" aria-label="Faint floral ornament"></div>
  <div class="back-decor back-decor--right" role="img" aria-label="Faint floral ornament"></div>
  <div class="back-frame"></div>

  <div class="list-panel">
    <div class="list-panel__inner">
      <ul class="service service--boxed">
        <li class="service__item"><div class="service__row">Hydration<span class="service__leader"></span><span class="service__price">$15</span></div><p class="service__desc">Lorem ipsum dolor sit, consectetuer adipiscing.</p></li>
        <li class="service__item"><div class="service__row">Mask<span class="service__leader"></span><span class="service__price">$10</span></div><p class="service__desc">Lorem ipsum dolo r sit, consectetuer adipiscing</p></li>
        <li class="service__item"><div class="service__row">Hair surgery<span class="service__leader"></span><span class="service__price">$20</span></div><p class="service__desc">Lorem ipsum dolor sit, consectetuer adipiscing.</p></li>
        <li class="service__item"><div class="service__row">Night Style<span class="service__leader"></span><span class="service__price">$15</span></div><p class="service__desc">Lorem ipsum dolor sit, consectetuer adipiscing.</p></li>
        <li class="service__item"><div class="service__row">Super Dry<span class="service__leader"></span><span class="service__price">$10</span></div><p class="service__desc">Lorem ipsum dolo r sit, consectetuer adipiscing</p></li>
        <li class="service__item"><div class="service__row">Diva Style<span class="service__leader"></span><span class="service__price">$20</span></div><p class="service__desc">Lorem ipsum dolor sit, consectetuer adipiscing.</p></li>
      </ul>
    </div>
  </div>

  <div class="tips">
    <div class="tips__inner">
      <h2 class="menu-box__title">TIPS</h2>
      <p class="tips__text">Lorem ipsum dolor sit amet, consectetuer adipiscing elit, sed diam nonummy nibh euismod tincidunt ut laoreet dolore magna aliquam erat volutpat. Ut wisi enim ad minim veniam, quis nostrud exerci tation ullamcorper suscipit lobortis nisl ut aliquip ex ea commodo consequat. Duis autem vel eum iriure dolor in hendrerit in vulputate velit esse molestie consequat, vel illum dolore eu feugiat nulla facilisis at vero eros et accumsan et iusto odio dignissim qui blandit praesent luptatum zzril delenit augue duis dolore te feugait nulla facilisi.</p>
    </div>
  </div>

  <div class="brand brand--cover"><span class="brand__mark"></span>VERBENA SALON</div>
  <div class="brand brand--foot"><span class="brand__mark"></span>VERBENA SALON</div>

  <div class="social social--back"><span class="social__icon"></span><span class="social__icon"></span><span class="social__icon"></span><span class="social__icon"></span></div>
</section>

</body>
</html>
```